Financial Sevices firm looking for Brochure design

Our company Veltmoor Capital and Holdings Limited (VeltHoldings)
i
Is an investment/advisory firm - www.veltholdings-grp.net
We invest in the energy sector in Africa and offer advisory services to Energy companies looking to invest in Africa. From oil and gas, to renewables (wind/solar). We are more focused on the "West African" Sub region
We need corporate brochure (Booklet style) to circulate to our corporate clients
We would like to see a design that considers the colours in our Logo (see website)
HI Guys, sorry been travelling. Seen some very good submissions and will be sending updates shortly
Reason: Dear Designers,
Thank you for participating in this project and for some of the great designs i've received so far. Unfortunately, due to the holidays, it has been difficult to consult with other members of my team. As a result, the project deadline is extended by about 12 days
I appreciate your understanding in the situation and looking forward to continuing the excellent collaboration in the coming days
Reason: Hi All,
Apologies for the multiple deadline extensions and thanks so much for all the designs which my team and I will be reviewing today and tomorrow.
We will be closing this project tomorrow by 6pm GMT (17th Jan 2014)
Thanks to all those that submitted such wonderful designs and goodluck!!
Project to be closed finally on 17th Jan 2014 at 6pm GMT
Banks, Investment Firms, Energy companies, Private Equity Funds
I have attached a Brochure that I created myself as an example of the type of information required but please also feel free to visit our website www.veltholdings-grp.net
Looking for any creative ideas you have to suplement the information provided.
Financial

```html
<!DOCTYPE html>
<html lang="en">
<head>
<meta charset="utf-8">
<title>VeltHoldings Brochure – Disclaimer Spread</title>
<link rel="stylesheet" href="https://fonts.googleapis.com/css2?family=PT+Sans:wght@400;700&display=swap">
<style>
  :root {
    --backdrop: #2b2b2b;
    --paper: #fbfbf9;
    --ink: #1e1e1e;
    --hill-green: #5f8a5a;
    --hill-teal: #7fa49a;
    --grass-yellow: #e2cf7a;
    --grass-gold: #c9b05a;
  }
  * { margin: 0; padding: 0; box-sizing: border-box; }
  html, body {
    width: 1200px;
    height: 793px;
    overflow: hidden;
    background: var(--backdrop);
  }
  .spread {
    position: absolute;
    left: 50px;
    top: 120px;
    width: 1100px;
    height: 552px;
    background: var(--paper);
    overflow: hidden;
  }
  .page {
    position: absolute;
    top: 0;
    width: 550px;
    height: 552px;
  }
  .page--left { left: 0; }
  .page--right { left: 550px; }
  .savanna {
    position: absolute;
    left: 0;
    bottom: 0;
    width: 1100px;
    height: 200px;
    background:
      linear-gradient(180deg,
        rgba(251,251,249,0) 0%,
        rgba(127,164,154,0.35) 40%,
        var(--hill-green) 66%,
        var(--grass-yellow) 78%,
        var(--grass-gold) 100%);
    -webkit-mask-image: linear-gradient(90deg, rgba(0,0,0,0.45) 0%, rgba(0,0,0,0.8) 35%, #000 60%);
            mask-image: linear-gradient(90deg, rgba(0,0,0,0.45) 0%, rgba(0,0,0,0.8) 35%, #000 60%);
  }
  .disclaimer {
    position: absolute;
    left: 92px;
    top: 122px;
    width: 372px;
    font-family: "PT Sans", sans-serif;
    font-size: 11.6px;
    line-height: 15.3px;
    color: var(--ink);
  }
  .disclaimer p + p { margin-top: 15.3px; }
  .brand {
    position: absolute;
    right: 14px;
    bottom: 30px;
    font-family: "PT Sans", sans-serif;
    font-size: 17px;
    line-height: 1;
    color: var(--ink);
  }
</style>
</head>
<body>
  <div class="spread">
    <div class="savanna" role="img" aria-label="Photograph of an acacia tree on a green hill above golden savanna grass, spanning both pages"></div>

    <section class="page page--left">
      <div class="disclaimer">
        <p>Veltmoor Capital and Holdings Limited (VeltHoldings) assumes no responsibility for any improper or incorrect use of information contained herein. Under no circumstances shall VeltHoldings be liable for any actions taken or omissions made from reliance on any information contained herein from whatever source nor shall VeltHoldings be liable for any other consequences from any such reliance. In no event shall VeltHoldings be held liable for any direct, indirect, incidental, special, exemplary or consequential damages or injury however caused and on any theory of liability, whether in contract, strict liability, or tort (including negligence or otherwise) arising in any way out of the use information contained herein, even if advised of the possibility of such damage or injury.</p>
        <p>Information or opinions provided by us in this document do not constitute an offer to sell or solicitation of an offer to buy any securities or financial instruments or any advice or recommendation with respect to such securities or other financial instruments or investments.</p>
      </div>
    </section>

    <section class="page page--right">
      <div class="brand">VeltHoldings</div>
    </section>
  </div>
</body>
</html>
```